Hair extension stockists

We need a logo and a packaging design, to show our range of hair extensions. We ideally want cream or black with an elegant feel. We would like a box that has a see through small element so that customers can see what colour is inside and we also want the box to open up from the side. Our name is Velomira Hair.This is for our standard range, in the next few months we will also have a luxury range. We are open to all ideas as we want to stand out from the rest.

Industry/Entity Type
Graphic Design

```html
<!DOCTYPE html>
<html lang="en">
<head>
<meta charset="utf-8">
<title>Velomira Hair – Standard Range Box Dieline</title>
<link rel="stylesheet" href="https://fonts.googleapis.com/css2?family=Inter:wght@300;400;700&display=swap">
<style>
  :root {
    --ink: #000000;
    --paper: #ffffff;
    --hair-dark: #141414;
    --hair-mid: #3a3c40;
    --hair-light: #8a8d93;
  }
  * { box-sizing: border-box; margin: 0; padding: 0; }
  html, body {
    width: 1200px;
    height: 714px;
    overflow: hidden;
    background: var(--paper);
    color: var(--ink);
    font-family: "Inter", "Helvetica Neue", Arial, sans-serif;
  }
  .dieline { position: relative; width: 1200px; height: 714px; }
  .panel {
    position: absolute;
    top: 47px;
    height: 590px;
    border: 1.5px solid var(--ink);
  }
  .panel--front  { left: 39px;  width: 337px; }
  .panel--side-a { left: 404px; width: 176px; }
  .panel--back   { left: 601px; width: 337px; }
  .panel--side-b { left: 965px; width: 176px; }

  .headline {
    position: absolute;
    left: 14px;
    top: 27px;
    font-weight: 700;
    font-size: 50px;
    line-height: 65px;
    letter-spacing: -0.5px;
  }
  .taglines {
    position: absolute;
    left: 14px;
    top: 294px;
    list-style: none;
    font-weight: 300;
    font-size: 18.5px;
    line-height: 25.5px;
  }
  .slash { font-weight: 700; }
  .taglines .brand { font-weight: 700; }

  .shade-name {
    position: absolute;
    left: 10px;
    top: 294px;
    font-weight: 300;
    font-size: 18.5px;
    line-height: 25.5px;
  }
  .shade-swatch {
    position: absolute;
    left: 9px;
    top: 332px;
    width: 154px;
    height: 244px;
    background:
      linear-gradient(160deg, var(--hair-mid) 0%, var(--hair-dark) 35%, var(--hair-mid) 55%, var(--hair-dark) 80%),
      var(--hair-dark);
  }
  .shade-swatch::after {
    content: "";
    position: absolute;
    inset: 0;
    background: radial-gradient(ellipse at 30% 10%, rgba(138,141,147,0.55), transparent 55%);
  }

  .imprint {
    position: absolute;
    left: 13px;
    bottom: 12px;
    font-size: 10.5px;
    line-height: 14.5px;
    font-weight: 400;
  }
  .imprint .ingredients { margin-top: 14.5px; }

  .panel-label {
    position: absolute;
    top: 657px;
    font-weight: 700;
    font-size: 19px;
    text-align: center;
  }
  .panel-label--front  { left: 39px;  width: 337px; }
  .panel-label--side-a { left: 404px; width: 176px; }
  .panel-label--back   { left: 601px; width: 337px; }
  .panel-label--side-b { left: 965px; width: 176px; }
</style>
</head>
<body>
<main class="dieline">
  <section class="panel panel--front">
    <h1 class="headline">100%<br>Human<br>Hair.</h1>
    <ul class="taglines">
      <li><span class="slash">/</span> extensions premium quality</li>
      <li><span class="slash">/</span> for more volume</li>
      <li><span class="slash">/</span> standard</li>
      <li class="brand">/ Velomira Hair</li>
    </ul>
  </section>

  <section class="panel panel--side-a">
    <p class="shade-name"><span class="slash">/</span> Jet Black</p>
    <div class="shade-swatch" role="img" aria-label="Close-up photo of glossy jet black hair"></div>
  </section>

  <section class="panel panel--back">
    <address class="imprint" style="font-style: normal;">
      <p>Velomira Hair<br>1001 Address<br>City<br>Country</p>
      <p class="ingredients">ingredients:<br>100% human hair</p>
    </address>
  </section>

  <section class="panel panel--side-b"></section>

  <p class="panel-label panel-label--front">FRONT</p>
  <p class="panel-label panel-label--side-a">SIDE</p>
  <p class="panel-label panel-label--back">BACK</p>
  <p class="panel-label panel-label--side-b">SIDE</p>
</main>
</body>
</html>
```